KO-TRA , Artificial hedge flyer

i need new flyer, in att i'm sending old one but as we produce artificial flowers, trees and most popular is artificial green hedge, and it's used from variety places, from swimming pool, restaurants, bars, private terrace, gardens, to protect from neighbor :-) . from beginning is all our product, it's not imported from other producer. we are doing it by measure what we get from customer ( tailor made ) , we give guaranty 15-20 years on all weather that will not loos color, etc.. you can see some pictures in att on old flyer, and some new pictures of same in space newly added. we'd like more pictures with samples of use, etc.you can see our product on www.ko-tra.hr so you can closely known what we are producing, and what for we need new flyer. we have plenty of new picture that are not on our web, so i can use it for new flyer.

Font styles to use
Sans Serif

Requirements
Must have
• company logo, contact info ( sent in word document in att ), logo of croatian product ( on old flyer in att on front side), stamp Quality since 1950 if you could change year to 1960, last time they made mistake and write 1950 ),
Nice to have
• flyer 3 fold type, or if you think it will look better only double side flyer, depend of design and theme so everyone can understand what is our business

```html
<!DOCTYPE html>
<html lang="hr">
<head>
<meta charset="utf-8">
<title>KO-TRA d.o.o. – trifold</title>
<link rel="stylesheet" href="https://fonts.googleapis.com/css2?family=Open+Sans:wght@400;600;700;800&family=Roboto+Condensed:wght@400;700&display=swap">
<style>
:root{
  --canvas:#e4e4e4;
  --label:#3c3c3c;
  --white:#ffffff;
  --green:#4f9a2c;
  --lime:#8cc63f;
  --deep:#1f3b1c;
  --hedge-a:#2f5a22;
  --hedge-b:#1b3517;
  --band:#5b5e60;
  --ink:#333333;
  --muted:#6b6b6b;
}
*{box-sizing:border-box;margin:0;padding:0}
html,body{width:1200px;height:4608px;overflow:hidden}
body{background:var(--canvas);font-family:"Open Sans",Arial,sans-serif;color:var(--ink);position:relative}
.fold-label{position:absolute;left:0;width:1200px;text-align:center;font-family:"Roboto Condensed",Arial,sans-serif;font-weight:700;font-size:40px;letter-spacing:2px;color:var(--label)}
.spread{position:absolute;left:60px;width:1080px;height:764px;overflow:hidden;background:var(--white);box-shadow:0 10px 30px rgba(0,0,0,.25)}
.panel{position:absolute;top:0;width:360px;height:764px;overflow:hidden}
.p1{left:0}.p2{left:360px}.p3{left:720px}
.photo{position:absolute}
.round{border-radius:50%;border:8px solid var(--white)}
.ring-green{border-color:var(--lime)}
.t-garden{background:linear-gradient(160deg,#7da55a,#3f6b2b 60%,#a8a79a)}
.t-map{background:linear-gradient(135deg,#eef0ea,#d9ded6 50%,#c8d7e6)}
.t-trees{background:linear-gradient(180deg,#8fb0c7,#3f6a3a 55%,#2d4c27)}
.t-pool{background:linear-gradient(170deg,#5f8f4a,#4fb5d6 45%,#2d8ab8 70%,#b9b7ae)}
.t-deck{background:linear-gradient(160deg,#5f8c3c,#8a4a2c 45%,#b0694a 75%,#d3cfc8)}
.t-hedge{background:radial-gradient(circle at 30% 20%,#3f7a2c,transparent 55%),linear-gradient(160deg,var(--hedge-a),var(--hedge-b))}
.t-terrace{background:linear-gradient(160deg,#8fb56e,#c7bca6 55%,#9c8f7e)}
.t-cars{background:linear-gradient(170deg,#6d9a4a,#9aa3aa 50%,#5b6066)}
.t-wall{background:linear-gradient(180deg,#3d7a2a,#d7cdbd 60%,#b9ab98)}
.t-court{background:linear-gradient(170deg,#4e8a36,#8fc06a 50%,#cfcfcf)}

.about{position:absolute;left:28px;top:34px;width:304px;font-size:11.5px;line-height:1.6;color:var(--muted)}
.about p+p{margin-top:10px}
.claim{position:absolute;left:24px;top:520px;width:310px;font-weight:800;font-size:19px;line-height:1.25;color:var(--white);text-shadow:0 1px 3px rgba(0,0,0,.4)}
.badge-years{position:absolute;left:24px;top:660px;width:76px;height:76px;border-radius:50%;background:var(--green);border:4px solid var(--white)}
.badge-origin{position:absolute;left:116px;top:672px;width:56px;height:56px;background:var(--white);border-radius:6px}

.curve-white{position:absolute}
.contact-head{position:absolute;left:196px;top:250px;font-weight:800;font-size:28px;color:var(--deep)}
.contact-address{position:absolute;left:196px;top:292px;width:150px;font-size:11.5px;line-height:1.5;color:var(--muted)}
.call-band{position:absolute;left:0;top:388px;width:360px;height:96px;background:var(--deep);color:var(--white);padding:12px 0 0 30px}
.call-band h3{font-size:20px;font-weight:700;color:var(--lime);margin-bottom:6px}
.phone-row{display:flex;align-items:center;gap:10px}
.phone-list{font-size:19px;font-weight:700;line-height:1.25}
.web-short{position:absolute;left:0;bottom:0;width:360px;height:76px;background:var(--deep);color:var(--white);font-weight:800;font-size:34px;display:flex;align-items:center;justify-content:center;letter-spacing:.5px}
.web-short::after{content:"";position:absolute;left:40px;right:40px;bottom:14px;height:2px;background:var(--lime)}

.brand{position:absolute;display:flex;align-items:center;gap:12px}
.brand-dot{width:34px;height:34px;border-radius:50%;background:var(--green);flex:none}
.brand-name{font-family:"Open Sans",Arial,sans-serif;font-weight:800;font-size:34px;color:var(--deep);letter-spacing:.5px;white-space:nowrap}
.brand-tag{position:absolute;font-size:16px;font-weight:600;color:var(--green);white-space:nowrap}
.cover-band{position:absolute;left:0;top:470px;width:360px;height:92px;background:var(--band);color:var(--white);font-family:"Roboto Condensed",Arial,sans-serif;font-size:21px;font-weight:400;line-height:1.25;text-transform:uppercase;padding:18px 22px}
.cover-strip{position:absolute;left:0;top:570px;width:360px;height:28px;background:var(--lime);color:var(--deep);font-size:10.5px;font-weight:700;text-align:center;line-height:28px;text-transform:uppercase}
.cover-web{position:absolute;right:22px;bottom:26px;font-weight:800;font-size:22px;color:var(--white)}

.inside{background:var(--hedge-b)}
.logo-bar{position:absolute;left:0;top:0;width:460px;height:96px;background:var(--white);border-bottom-right-radius:60px}
.inside-text{position:absolute;left:44px;top:310px;width:272px;height:330px;background:rgba(20,40,18,.88);color:var(--white);padding:26px 22px;font-size:17px;line-height:1.45;text-align:center}
.motto{position:absolute;left:24px;top:668px;width:312px;text-align:center;font-weight:800;font-size:28px;color:var(--white);white-space:nowrap}
.benefits{position:absolute;left:24px;top:250px;width:312px;height:270px;background:var(--white);border-radius:8px;padding:20px 20px}
.benefits h3{font-weight:800;font-size:26px;color:var(--green);margin-bottom:6px}
.benefits ul{list-style:none}
.benefits li{display:flex;gap:8px;font-size:12.5px;line-height:1.45;color:var(--ink);margin-bottom:6px;font-weight:600}
.benefits li svg{flex:none;margin-top:3px}
.quality-head{position:absolute;left:24px;top:540px;width:312px;background:var(--green);color:var(--white);font-weight:700;font-size:18px;padding:10px 16px}
.quality-note{position:absolute;left:24px;top:584px;width:312px;background:var(--white);font-size:11.5px;line-height:1.5;color:var(--muted);padding:10px 16px;height:70px}
.plain-badge{position:absolute;border-radius:50%}
</style>
</head>
<body>

<h2 class="fold-label" style="top:150px">OUTSIDE FOLD</h2>

<section class="spread" style="top:230px" aria-label="Vanjska strana letka">
  <div class="panel p1">
    <div class="about">
      <p>Tvrtka KO-TRA d.o.o. osnovana je kao obiteljska proizvodnja umjetnog cvijeća, drveća i živica. Sve proizvode izrađujemo sami u vlastitoj radionici, bez uvoza od drugih proizvođača.</p>
      <p>Umjetnu živicu radimo po mjeri koju nam pošaljete, za bazene, restorane, kafiće, terase i vrtove. Na boju i postojanost dajemo jamstvo od 15 do 20 godina u svim vremenskim uvjetima.</p>
    </div>
    <div class="photo t-garden" style="left:0;top:400px;width:360px;height:364px" role="img" aria-label="Fotografija vrta s umjetnom živicom i kuglama zelenila"></div>
    <p class="claim">Umjetna živica koja izgleda kao prava, cijele godine</p>
    <div class="badge-years" role="img" aria-label="Oznaka godina tradicije"></div>
    <div class="badge-origin" role="img" aria-label="Oznaka hrvatskog proizvoda"></div>
  </div>

  <div class="panel p2">
    <div class="photo t-map" style="left:0;top:0;width:360px;height:150px" role="img" aria-label="Karta s lokacijom tvrtke"></div>
    <svg style="position:absolute;left:250px;top:46px" width="26" height="36" viewBox="0 0 26 36"><path d="M13 0C6 0 0 6 0 13c0 9 13 23 13 23s13-14 13-23C26 6 20 0 13 0z" fill="#c0392b"/><circle cx="13" cy="13" r="5" fill="#fff"/></svg>
    <div class="photo t-trees" style="left:0;top:150px;width:200px;height:238px" role="img" aria-label="Fotografija ulaza s visokim umjetnim drvećem"></div>
    <svg class="curve-white" style="left:150px;top:120px" width="210" height="268" viewBox="0 0 210 268"><path d="M0 268 C30 150 90 60 210 30 L210 268Z" fill="#fff"/></svg>
    <h3 class="contact-head">kontakt</h3>
    <p class="contact-address">Ulica Lipa 12, Zagreb<br>info@ko-tra.hr</p>
    <div class="call-band">
      <h3>Nazovite nas</h3>
      <div class="phone-row">
        <svg width="30" height="30" viewBox="0 0 24 24" aria-hidden="true"><path d="M6.6 10.8a15 15 0 0 0 6.6 6.6l2.2-2.2a1 1 0 0 1 1-.25 11.4 11.4 0 0 0 3.6.57 1 1 0 0 1 1 1V20a1 1 0 0 1-1 1A17 17 0 0 1 3 4a1 1 0 0 1 1-1h3.5a1 1 0 0 1 1 1c0 1.25.2 2.45.57 3.57a1 1 0 0 1-.25 1z" fill="#8cc63f"/></svg>
        <div class="phone-list">+385 91 555 0142<br>+385 91 555 0187</div>
      </div>
    </div>
    <div class="photo t-pool" style="left:0;top:484px;width:360px;height:204px" role="img" aria-label="Fotografija bazena okruženog umjetnom živicom"></div>
    <div class="web-short">ko-tra.hr</div>
  </div>

  <div class="panel p3 t-hedge" role="img" aria-label="Pozadina od zelene umjetne živice">
    <div class="photo t-deck" style="left:0;top:0;width:360px;height:330px" role="img" aria-label="Fotografija drvene terase uz umjetnu živicu"></div>
    <svg class="curve-white" style="left:0;top:250px" width="360" height="200" viewBox="0 0 360 200"><path d="M0 120 C90 40 220 10 360 60 L360 200 L0 200Z" fill="#fff"/></svg>
    <div class="brand" style="left:30px;top:350px"><span class="brand-dot"></span><span class="brand-name">KO-TRA d.o.o.</span></div>
    <p class="brand-tag" style="left:78px;top:400px">Zelenilo po mjeri</p>
    <div class="cover-band">Umjetna živica za unutarnje i vanjsko uređenje prostora</div>
    <div class="cover-strip">Vlastita proizvodnja · jamstvo do 20 godina</div>
    <div class="cover-web">www.ko-tra.hr</div>
  </div>
</section>

<h2 class="fold-label" style="top:2420px">INSIDE FOLD</h2>

<section class="spread inside" style="top:2500px" aria-label="Unutarnja strana letka">
  <div class="panel p1 t-hedge" role="img" aria-label="Pozadina od zelene umjetne živice">
    <div class="photo round t-terrace" style="left:20px;top:120px;width:170px;height:170px" role="img" aria-label="Fotografija terase s cvijećem"></div>
    <div class="photo round t-court" style="left:190px;top:230px;width:140px;height:140px" role="img" aria-label="Fotografija dvorišta sa živicom"></div>
    <div class="photo t-cars" style="left:0;top:380px;width:360px;height:140px" role="img" aria-label="Fotografija parkirališta ograđenog živicom"></div>
    <div class="photo round t-pool" style="left:20px;top:520px;width:170px;height:170px" role="img" aria-label="Fotografija bazena s živicom"></div>
    <div class="photo t-wall" style="left:190px;top:560px;width:170px;height:204px" role="img" aria-label="Fotografija zida s umjetnom živicom"></div>
    <div class="plain-badge" style="left:230px;top:640px;width:80px;height:80px;background:#f3efe6" role="img" aria-label="Oznaka kvalitete"></div>
  </div>
  <div class="logo-bar">
    <div class="brand" style="left:30px;top:18px"><span class="brand-dot"></span><span class="brand-name">KO-TRA d.o.o.</span></div>
    <p class="brand-tag" style="left:78px;top:64px">Zelenilo po mjeri</p>
  </div>

  <div class="panel p2 t-hedge" role="img" aria-label="Pozadina od zelene umjetne živice">
    <div class="photo round t-deck" style="left:150px;top:110px;width:190px;height:190px" role="img" aria-label="Fotografija stola na terasi uz živicu"></div>
    <div class="inside-text">Umjetnu živicu izrađujemo prema mjerama i dimenzijama koje Vam trebaju, dostavimo na Vašu adresu kako bi se Vama napravila umjetna živica prema Vašim željama i idejama.</div>
    <p class="motto">Zelenilo po mjeri</p>
  </div>

  <div class="panel p3 t-hedge" role="img" aria-label="Pozadina od zelene umjetne živice">
    <div class="photo round ring-green t-court" style="left:150px;top:20px;width:200px;height:200px" role="img" aria-label="Fotografija terase s umjetnom živicom"></div>
    <div class="benefits">
      <h3>Prednosti</h3>
      <ul>
        <li><svg width="14" height="12" viewBox="0 0 14 12"><path d="M1 6l4 4 8-9" stroke="#4f9a2c" stroke-width="2.5" fill="none"/></svg>Ne zahtijeva zalijevanje ni orezivanje</li>
        <li><svg width="14" height="12" viewBox="0 0 14 12"><path d="M1 6l4 4 8-9" stroke="#4f9a2c" stroke-width="2.5" fill="none"/></svg>Ne gubi boju 15 do 20 godina</li>
        <li><svg width="14" height="12" viewBox="0 0 14 12"><path d="M1 6l4 4 8-9" stroke="#4f9a2c" stroke-width="2.5" fill="none"/></svg>Otporna na sve vremenske uvjete</li>
        <li><svg width="14" height="12" viewBox="0 0 14 12"><path d="M1 6l4 4 8-9" stroke="#4f9a2c" stroke-width="2.5" fill="none"/></svg>Izrada po mjeri kupca</li>
        <li><svg width="14" height="12" viewBox="0 0 14 12"><path d="M1 6l4 4 8-9" stroke="#4f9a2c" stroke-width="2.5" fill="none"/></svg>Štiti privatnost od pogleda susjeda</li>
      </ul>
    </div>
    <div class="quality-head">Prepoznaj kvalitetu</div>
    <p class="quality-note">Svi proizvodi nastaju u našoj radionici, od materijala provjerene kvalitete.</p>
    <div class="plain-badge" style="left:30px;top:672px;width:76px;height:76px;background:var(--green);border:4px solid #fff" role="img" aria-label="Oznaka godina tradicije"></div>
    <div class="plain-badge" style="left:122px;top:680px;width:60px;height:60px;background:#fff;border-radius:6px" role="img" aria-label="Oznaka hrvatskog proizvoda"></div>
  </div>
</section>

</body>
</html>
```